Frostglen Fair LV, A Magical Holiday Festival

frostglenfairlv-example.com
Need to include the following:
Dates: Dec 14- Dec 30
kids 48'' and under free, presale tickets $6, glimmer pass $25(17 days pass) website: frostglenfairlv-example.com, ice skating rink, snow park, santa house, first 1000 kids will receive a gift from Santa on Christmas day.
Location: Brambleton Lodge, 4187 Quillstone Avenue.
Also need to include QRM logo and Grand Copperfield Supper Fair logo (I attached)

Industry/Entity Type

Festival

Font styles to use
Decorative

Requirements
Must have
• Date : December 14- December 30
• Location: Brambleton Lodge
Nice to have
• Santa House, christmas lights, ice skating rink, snow park

```html
<!DOCTYPE html>
<html lang="en">
<head>
<meta charset="utf-8">
<title>Frostglen Fair LV – Tickets &amp; Schedule</title>
<link href="https://fonts.googleapis.com/css2?family=Cinzel:wght@700&family=Playfair+Display:wght@500&family=Questrial&family=Oswald:wght@400&display=swap" rel="stylesheet">
<style>
  :root {
    --backdrop: #c3eefb;
    --board: #3a3a3b;
    --board-dark: #2b2b2c;
    --gold: #f2c12e;
    --gold-soft: #e8c56a;
    --cream: #f3ead2;
    --white: #ffffff;
    --line: #141414;
    --ink: #1d1d1f;
  }
  * { margin: 0; padding: 0; box-sizing: border-box; }
  html, body { width: 1200px; height: 1200px; overflow: hidden; }
  body { background: var(--backdrop); position: relative; }

  .flyer {
    position: absolute; left: 200px; top: 35px;
    width: 800px; height: 1130px; overflow: hidden;
    background: linear-gradient(180deg, var(--board) 0%, var(--board-dark) 100%);
    font-family: "Questrial", sans-serif; color: var(--white);
  }
  .flyer > * { position: absolute; }
  .center { left: 0; width: 100%; text-align: center; }

  .lights-scene {
    left: 0; top: 0; width: 100%; height: 330px;
    background: linear-gradient(180deg, #4a4036 0%, #5c4a38 35%, rgba(58,58,59,0) 100%);
  }

  .brand-name { top: 62px; font-family: "Playfair Display", serif; font-weight: 500; font-size: 46px; line-height: 1; color: var(--white); }
  .brand-tagline { top: 152px; font-family: "Playfair Display", serif; font-size: 10px; letter-spacing: 1px; color: var(--white); }

  .title { top: 180px; font-family: "Cinzel", serif; font-weight: 700; font-size: 42px; color: var(--gold-soft); letter-spacing: 1px; }
  .intro { top: 236px; font-size: 16px; color: var(--gold); }
  .intro b { color: var(--white); font-weight: normal; }
  .event-name { top: 262px; font-size: 30px; color: var(--gold-soft); }
  .dates { top: 312px; font-size: 28px; color: var(--white); }
  .dates span, .location span { color: var(--gold); }
  .location { top: 352px; font-size: 17px; color: var(--white); }

  .panel { left: 48px; width: 702px; border: 2px solid var(--line); border-radius: 26px; }
  .schedule-panel { top: 417px; height: 320px; }
  .pricing-panel { top: 777px; height: 112px; }
  .panel-heading {
    font-size: 27px; color: var(--gold); background: var(--board);
    padding: 0 16px; left: 50%; transform: translate(-50%, -50%); white-space: nowrap;
  }
  .schedule-heading { top: 416px; background: #393939; }
  .pricing-heading { top: 776px; background: #323233; }

  .slot { font-family: "Oswald", sans-serif; line-height: 1; }
  .slot .day { display: block; font-size: 13.5px; color: var(--gold); }
  .slot .time { display: block; font-size: 11px; color: var(--white); margin-top: 9px; }
  .final-slot { top: 707px; font-family: "Oswald", sans-serif; font-size: 13.5px; }
  .final-slot .day { color: var(--gold); margin-right: 26px; }

  .price-row { top: 800px; left: 76px; width: 660px; height: 36px; font-family: "Oswald", sans-serif; font-size: 16px; color: var(--gold); }
  .price-row > * { position: absolute; top: 50%; transform: translateY(-50%); white-space: nowrap; }
  .price-badge { width: 38px; height: 38px; border-radius: 50%; background: var(--gold); color: var(--ink); text-align: center; line-height: 38px; font-size: 16px; }
  .price-row .divider { color: var(--white); }
  .price-row .note { font-size: 13px; }
  .rule { top: 847px; left: 86px; width: 630px; height: 1px; background: #6b6b6b; }
  .gift-note { top: 855px; font-size: 19px; color: var(--white); }
  .gift-note span { color: var(--gold); }

  .village-scene {
    left: 0; top: 895px; width: 100%; height: 235px;
    background: linear-gradient(180deg, rgba(58,58,59,0) 0%, #9a9fa6 35%, #e9ecef 62%, #ffffff 78%);
  }
  .partners { top: 1062px; left: 0; width: 100%; height: 20px; font-size: 13px; color: var(--ink); }
  .partners span { position: absolute; white-space: nowrap; transform: translateX(-50%); }
  .website { top: 1094px; font-size: 17px; letter-spacing: 4.5px; color: var(--ink); }
</style>
</head>
<body>
<main class="flyer">
  <div class="lights-scene" role="img" aria-label="Coloured Christmas string lights hanging over bare winter trees"></div>

  <h1 class="brand-name center">Frostglen Fair</h1>
  <p class="brand-tagline center">A MAGICAL HOLIDAY FESTIVAL</p>

  <h2 class="title center">Tickets &amp; Schedule</h2>
  <p class="intro center">This year calls for <b>17 DAYS</b> of snow in a Frostglen Fair of fun!</p>
  <p class="event-name center">Frostglen Fair Las Vegas</p>
  <p class="dates center"><span>DATES :</span> Dec 14- Dec 30, 2017</p>
  <p class="location center"><span>LOCATION:</span> Brambleton Lodge, 4187 Quillstone Avenue.</p>

  <div class="panel schedule-panel"></div>
  <h3 class="panel-heading schedule-heading">EVENT DATES &amp; TIME</h3>

  <div class="slot" style="left:73px;top:452px"><span class="day">THU, DEC 14, 2017</span><span class="time">2 PM – 10:00 PM PST</span></div>
  <div class="slot" style="left:242px;top:452px"><span class="day">FRI, DEC 15, 2017</span><span class="time">2:00 PM – 10:00 PM PST</span></div>
  <div class="slot" style="left:419px;top:452px"><span class="day">SAT, DEC 16, 2017</span><span class="time">12:00 PM – 10:00 PM PST</span></div>
  <div class="slot" style="left:606px;top:452px"><span class="day">SUN, DEC 17, 2017</span><span class="time">12:00 PM – 10:00 PM PST</span></div>

  <div class="slot" style="left:73px;top:512px"><span class="day">MON, DEC 18, 2017</span><span class="time">2:00 PM – 10:00 PM PST</span></div>
  <div class="slot" style="left:242px;top:512px"><span class="day">TUE, DEC 19, 2017</span><span class="time">2:00 PM – 10:00 PM PST</span></div>
  <div class="slot" style="left:419px;top:512px"><span class="day">WED, DEC 20, 2017</span><span class="time">2:00 PM – 10:00 PM PST</span></div>
  <div class="slot" style="left:606px;top:512px"><span class="day">THU, DEC 21, 2017</span><span class="time">2:00 PM – 10:00 PM PST</span></div>

  <div class="slot" style="left:73px;top:574px"><span class="day">FRI, DEC 22, 2017</span><span class="time">2:00 PM – 10:00 PM PST</span></div>
  <div class="slot" style="left:242px;top:574px"><span class="day">SAT, DEC 23, 2017</span><span class="time">12:00 PM – 10:00 PM PST</span></div>
  <div class="slot" style="left:419px;top:574px"><span class="day">SUN, DEC 24, 2017</span><span class="time">2:00 PM – 8:00PM PST</span></div>
  <div class="slot" style="left:606px;top:574px"><span class="day">MON, DEC 25, 2017</span><span class="time">2:00 PM – 9:00 PM PST</span></div>

  <div class="slot" style="left:73px;top:641px"><span class="day">TUE, DEC 26, 2018</span><span class="time">2:00 PM – 10:00 PM PST</span></div>
  <div class="slot" style="left:242px;top:641px"><span class="day">WED, DEC 27, 2017</span><span class="time">2:00 PM – 10:00 PM PST</span></div>
  <div class="slot" style="left:419px;top:641px"><span class="day">THU, DEC 28, 2017</span><span class="time">2:00 PM – 10:00 PM PST</span></div>
  <div class="slot" style="left:606px;top:641px"><span class="day">FRI, DEC 29, 2017</span><span class="time">2:00PM – 11:00PM PST</span></div>

  <p class="final-slot center"><span class="day">SAT, DEC 30, 2017</span><span>12:00 PM – 11:00 PM PST</span></p>

  <div class="panel pricing-panel"></div>
  <h3 class="panel-heading pricing-heading">TICKET PRICING:</h3>

  <div class="price-row">
    <span style="left:0">kids 48'' and under free, presale tickets</span>
    <span class="price-badge" style="left:285px">$0</span>
    <span class="divider" style="left:371px">|</span>
    <span style="left:400px">GLIMMER PASS</span>
    <span class="price-badge" style="left:503px">$25</span>
    <span class="note" style="left:565px">(17 DAYS PASS)</span>
  </div>
  <div class="rule"></div>
  <p class="gift-note center"><span>FIRST 1000 KIDS</span> will receive <span>A GIFT</span> from Santa on Christmas day.</p>

  <div class="village-scene" role="img" aria-label="Paper-cut snowy village with decorated Christmas trees and red gift boxes on both sides"></div>

  <div class="partners">
    <span style="left:330px">Grand Copperfield Supper Fair</span>
    <span style="left:470px">QRM</span>
  </div>
  <p class="website center">frostglenfairlv-example.com</p>
</main>
</body>
</html>
```